Business card design needed

We are a Custom Joinery and specialise in design, Manufacture and Installation of kitchens and cabinetry
We currently have a logo based on the northern star in red and black but are open to something that would look fresh and clean
Updates

Project Deadline Extended
Reason: Need a couple days to go through designs. Finding some designs that are great on front and others great on reverse. I would like to be able to comment and get the total look we are after.

Target Market(s)

30-50 year olds who are looking to renovate

Industry/Entity Type

Business

Contact Information for Business Card

Maple Crest Interiors
ABN 37 418 260 503
Carlo Whitby - Cabinetmaker/Designer Licence No. 581907K

Requirements
Nice to have
• Maybe a nice fresh modern kitchen picture

```html
<!DOCTYPE html>
<html lang="en">
<head>
<meta charset="utf-8">
<title>Maple Crest Interiors – Business Card</title>
<link rel="stylesheet" href="https://fonts.googleapis.com/css2?family=Tenor+Sans&display=swap">
<style>
  :root {
    --card-bg: #ffffff;
    --card-border: #8a8a8a;
    --brand-ink: #151515;
    --accent-red: #e3202d;
  }
  html, body {
    margin: 0;
    padding: 0;
    width: 1200px;
    height: 693px;
    overflow: hidden;
    background: var(--card-bg);
  }
  .business-card {
    position: relative;
    box-sizing: border-box;
    width: 1200px;
    height: 693px;
    background: var(--card-bg);
    border: 2px solid var(--card-border);
    font-family: "Tenor Sans", "Optima", sans-serif;
  }
  .brand-name {
    position: absolute;
    left: 0;
    right: 0;
    top: 300px;
    margin: 0;
    text-align: center;
    font-size: 60px;
    font-weight: 400;
    letter-spacing: 3px;
    line-height: 1;
    color: var(--brand-ink);
  }
  .contact-details {
    position: absolute;
    left: 0;
    right: 0;
    top: 574px;
    margin: 0;
    text-align: center;
    color: var(--accent-red);
    font-weight: 400;
  }
  .contact-details .name-role {
    display: block;
    font-size: 31px;
    letter-spacing: 1.5px;
    line-height: 1;
  }
  .contact-details .registration {
    display: block;
    margin-top: 12px;
    font-size: 26px;
    letter-spacing: 1.5px;
    line-height: 1;
  }
</style>
</head>
<body>
  <main class="business-card">
    <h1 class="brand-name">MAPLE CREST INTERIORS</h1>
    <p class="contact-details">
      <span class="name-role">CARLO WHITBY &nbsp;|&nbsp; CABINETMAKER/DESIGNER</span>
      <span class="registration">LICENCE NO. 581907K &nbsp;|&nbsp; ABN 37 418 260 503</span>
    </p>
  </main>
</body>
</html>
```